Rollers & Glides.com

Vertical Business Card with focus on branding with our icon. Information on card will be logo, persons name, position, phone number, email address and website. Use the the name Marcus Delby, position President, phone number 480.315.7792, email Marcus@rollersandglides-example.com, website www.rollersandglides-example.com.

```html
<!DOCTYPE html>
<html lang="en">
<head>
<meta charset="utf-8">
<title>Rollers &amp; Glides.com — Business Card</title>
<link href="https://fonts.googleapis.com/css2?family=Roboto:wght@400;500;700&display=swap" rel="stylesheet">
<style>
  :root {
    --backdrop: #e4e4e4;
    --card: #f1f0ef;
    --ink: #222222;
    --ink-soft: #333333;
    --card-shadow: rgba(0, 0, 0, 0.18);
  }
  * { box-sizing: border-box; margin: 0; padding: 0; }
  html, body {
    width: 1200px;
    height: 750px;
    overflow: hidden;
    background: var(--backdrop);
    font-family: "Roboto", Arial, sans-serif;
    color: var(--ink);
  }
  .stage {
    position: relative;
    width: 1200px;
    height: 750px;
  }
  .card {
    position: absolute;
    top: 139px;
    width: 270px;
    height: 472px;
    background: var(--card);
    box-shadow: 8px 10px 24px var(--card-shadow);
    overflow: hidden;
  }
  .card--front { left: 295px; }
  .card--back { left: 637px; }

  .brand {
    position: absolute;
    left: 0;
    right: 0;
    display: flex;
    align-items: center;
    justify-content: center;
    gap: 12px;
  }
  .card--front .brand { top: 70px; }
  .card--back .brand { top: 196px; }
  .brand__mark {
    width: 66px;
    height: 66px;
    border: 3px solid var(--ink);
    border-radius: 50%;
    flex: none;
  }
  .brand__name {
    font-family: "Roboto", Arial, sans-serif;
    font-weight: 400;
    font-size: 22px;
    line-height: 1.05;
    color: var(--ink);
  }

  .contact {
    position: absolute;
    top: 270px;
    left: 0;
    right: 0;
    text-align: center;
  }
  .contact__name {
    font-weight: 700;
    font-size: 17px;
    letter-spacing: 0.3px;
    text-transform: uppercase;
    color: var(--ink);
  }
  .contact__role {
    margin-top: 2px;
    font-size: 11.5px;
    letter-spacing: 1.6px;
    text-transform: uppercase;
    color: var(--ink-soft);
  }
  .contact__icons {
    display: flex;
    justify-content: center;
    gap: 12px;
    margin-top: 14px;
  }
  .contact__icons svg { width: 15px; height: 15px; }
  .contact__lines {
    list-style: none;
    margin-top: 12px;
    font-size: 11.5px;
    letter-spacing: 0.9px;
    color: var(--ink-soft);
  }
  .contact__lines li { line-height: 22px; }
  .contact__dash {
    width: 11px;
    height: 1.5px;
    background: var(--ink);
    margin: 14px auto 0;
  }
</style>
</head>
<body>
<main class="stage">
  <section class="card card--front" aria-label="Business card front">
    <div class="brand">
      <span class="brand__mark" aria-hidden="true"></span>
      <span class="brand__name">Rollers &amp;<br>Glides.com</span>
    </div>
    <div class="contact">
      <h1 class="contact__name">Marcus Delby</h1>
      <p class="contact__role">President</p>
      <div class="contact__icons" aria-hidden="true">
        <svg viewBox="0 0 16 16" fill="none" stroke="#222" stroke-width="1">
          <circle cx="8" cy="8" r="7.2"/>
          <path d="M5.3 4.6l1.3-.3.8 1.8-.9.7c.5 1.1 1.3 1.9 2.4 2.4l.7-.9 1.8.8-.3 1.3c-3.1.1-5.9-2.7-5.8-5.8z" fill="#222" stroke="none"/>
        </svg>
        <svg viewBox="0 0 16 16" fill="none" stroke="#222" stroke-width="1">
          <circle cx="8" cy="8" r="7.2"/>
          <rect x="4.4" y="5.4" width="7.2" height="5.2" fill="#222" stroke="none"/>
          <path d="M4.6 5.6L8 8.4l3.4-2.8" stroke="#f1f0ef" stroke-width="0.8"/>
        </svg>
        <svg viewBox="0 0 16 16" fill="none" stroke="#222" stroke-width="1">
          <circle cx="8" cy="8" r="7.2"/>
          <circle cx="8" cy="8" r="3.8"/>
          <path d="M8 4.2v7.6M4.2 8h7.6" stroke-width="0.7"/>
        </svg>
      </div>
      <ul class="contact__lines">
        <li>480.315.7792</li>
        <li>Marcus@rollersandglides-example.com</li>
        <li>rollersandglides-example.com</li>
      </ul>
      <div class="contact__dash" aria-hidden="true"></div>
    </div>
  </section>

  <section class="card card--back" aria-label="Business card back">
    <div class="brand">
      <span class="brand__mark" aria-hidden="true"></span>
      <span class="brand__name">Rollers &amp;<br>Glides.com</span>
    </div>
  </section>
</main>
</body>
</html>
```